Steady Yield Contract Playbooks for busy people

"Necessity is the mother of invention"

The idea of vetting investment strategies is not new in the financial world before investing real monies. Vetting strategies in options strategies always have been a difficult exercise. Such exercise requires access to programmers, right tools and good historical data. These factors make vetting process very costly and tedious. Becuase of this reason, this process is mostly limited to hedge funds, private banking, wealth management firms. Very few products existed in the market to support this process.

Since my graduation in engineering with major in Computer Science, I worked in large global banks as an IT consultant. Over there, I was designing, developing or managing large IT projects. This job profile demanded long hours, busy and tiring days. Very few hours or literally, not enough time available to analyze investment opportunities.

Moreover, investing in stocks without understanding valuation, business model and financials of the companies often result in losses. More so, if not enough understanding on when to exit from a position. Entering into a position is easy and it is in trader's control but exiting a position when profiting and cutting losses is an important step to make money consistently. This needed more disciplined approach and defined rules for position sizing, money management, profit taking and cutting losses.

Options have greeks that will affect its pricing. Understanding and leading options is another major step in the hurdle of investing in options. There are good mentors/experts teaching options. Gaining conceptual understanding is not that difficult. Practically seeing the market affecting the options trades is the most difficult step. Mentors/experts use primitive tools that give some peek into the practical process but it is very tedious since they often provide manual backtesting. "Options" provide options. There are a lot of questions that need to be answered.

Which options strategy is right?
How to select the expiration date for each options strategy?
How to select the strikes involved in options strategy?
There is an option to paper trade and gain knowledge in these areas. But it is a slow process. To speed things up, I founded Korvane platform which speeds up vetting process. Moreover, all the tests done in the process of strategy design is remembered by the platform. If there a study that can deliver reward expectations for the acceptable risk amount, it can be locked to produce the trading opportunities on any interval. This makes it easy to use model for busy people.

The rest of the book is not to make you experts in all trading areas but it is targeted to help busy people with enough understanding to help you learn, trade carefully knowing that options trading has different risk characteristics. You can refer to them in detail on PWT website. All studies published in this book does not guarantee a future success but they have produced results in the past. These should be taken as educational reference.
Updates

This design is for Print book. Below is about the author. Book needs to have bar code printed and ISBN listed on the back as well. Tomas Brennick, Founder, Korvane Markets Tomas is a computer science engineer with more than two decades of experience working for major financial institutions Vuma, RT Holdings, and PLWN. During his time at Orlundt Advisory Services, he spearheaded a large global delivery team, led business growth in Latin America from the ground up, and was directly responsible for customer experience and software delivery. During this time, he discovered the passion for trading options. Leveraging this against his extensive experience in computer software architecture, Tomas ventured out on his own to found and created www.korvanemarkets.example

Target Market(s)

Busy people with money and want to invest in stock market

Industry/Entity Type

Investment

Font styles to use
Sans Serif

Colors

Designer to choose colors to be used in the design.

Requirements
Must have
• 6 x 9 book. Title of book is "Steady Yield Contract Playbooks" and the subtitle is "for busy people". The author is Tomas Brennick.
• This is soft cover with 155 pages

```html
<!DOCTYPE html>
<html lang="en">
<head>
<meta charset="utf-8">
<title>Steady Yield Contract Playbooks — Tomas Brennick</title>
<link rel="stylesheet" href="https://fonts.googleapis.com/css2?family=Montserrat:ital,wght@0,400;0,700;0,800;1,800;1,900&display=swap">
<style>
  :root {
    --cover-green: #2aa57e;
    --cover-green-light: #35b38b;
    --ink-navy: #2b3160;
    --paper-white: #ffffff;
    --brand-blue: #22306b;
  }
  * { margin: 0; padding: 0; box-sizing: border-box; }
  html, body { width: 800px; height: 1200px; overflow: hidden; background: var(--cover-green); }
  .cover {
    position: relative;
    width: 800px;
    height: 1200px;
    background: var(--cover-green);
    font-family: "Montserrat", Arial, sans-serif;
    overflow: hidden;
  }
  .publisher-flag {
    position: absolute;
    left: 0;
    top: 0;
    width: 580px;
    height: 205px;
  }
  .publisher-mark {
    position: absolute;
    left: 78px;
    top: 62px;
    display: flex;
    align-items: center;
    gap: 14px;
  }
  .publisher-dot {
    width: 54px;
    height: 54px;
    border-radius: 50%;
    background: var(--brand-blue);
  }
  .publisher-name {
    font-weight: 800;
    font-size: 54px;
    line-height: 1;
    color: var(--brand-blue);
  }
  .publisher-presents {
    position: absolute;
    left: 148px;
    top: 120px;
    font-weight: 800;
    font-size: 22px;
    letter-spacing: 4px;
    color: var(--brand-blue);
  }
  .finance-icons-top {
    position: absolute;
    left: 170px;
    top: 200px;
    width: 440px;
    height: 70px;
    border-radius: 8px;
    background: linear-gradient(90deg, rgba(255,255,255,0.18), rgba(255,255,255,0.28), rgba(255,255,255,0.18));
  }
  .title-rule {
    position: absolute;
    left: 300px;
    top: 302px;
    width: 420px;
    border-top: 4px dashed var(--paper-white);
  }
  .book-title {
    position: absolute;
    left: 110px;
    top: 268px;
    font-style: italic;
    font-weight: 900;
    text-transform: uppercase;
    line-height: 0.95;
  }
  .title-line { display: block; font-size: 100px; letter-spacing: 1px; }
  .title-line--light {
    color: var(--paper-white);
    text-shadow: 6px 6px 0 var(--ink-navy);
  }
  .title-line--dark {
    color: var(--ink-navy);
    text-shadow: 5px 5px 0 var(--paper-white);
  }
  .title-line--first { font-size: 112px; margin-bottom: 8px; }
  .subtitle-box {
    position: absolute;
    left: 300px;
    top: 688px;
    padding: 10px 26px;
    background: var(--ink-navy);
    outline: 3px dashed var(--paper-white);
    outline-offset: -9px;
    color: var(--paper-white);
    font-weight: 700;
    font-size: 34px;
    letter-spacing: 1px;
    text-transform: uppercase;
  }
  .subtitle-rule {
    position: absolute;
    left: 120px;
    top: 806px;
    width: 600px;
    border-top: 3px dashed rgba(255,255,255,0.8);
  }
  .finance-icons-bottom {
    position: absolute;
    left: 260px;
    top: 840px;
    width: 300px;
    height: 90px;
    border-radius: 8px;
    background: linear-gradient(90deg, rgba(255,255,255,0.15), rgba(43,49,96,0.25), rgba(255,255,255,0.15));
  }
  .author {
    position: absolute;
    left: 0;
    width: 800px;
    top: 980px;
    text-align: center;
    color: var(--paper-white);
    font-size: 44px;
    letter-spacing: 1px;
    text-transform: uppercase;
  }
  .author-first { font-weight: 400; }
  .author-last { font-weight: 800; }
</style>
</head>
<body>
<main class="cover">
  <svg class="publisher-flag" viewBox="0 0 580 205" aria-hidden="true">
    <polygon points="0,0 580,0 520,100 580,205 0,205" fill="#ffffff"/>
  </svg>
  <div class="publisher-mark">
    <span class="publisher-dot"></span>
    <span class="publisher-name">Korvane</span>
  </div>
  <div class="publisher-presents">PRESENTS</div>

  <div class="finance-icons-top" role="img" aria-label="Row of small line-art finance icons: charts, coins, money bag and gears"></div>
  <div class="title-rule"></div>

  <h1 class="book-title">
    <span class="title-line title-line--light title-line--first">Steady</span>
    <span class="title-line title-line--dark">Yield</span>
    <span class="title-line title-line--light">Contract</span>
    <span class="title-line title-line--dark">Playbooks</span>
  </h1>

  <div class="subtitle-box">For busy people</div>
  <div class="subtitle-rule"></div>

  <div class="finance-icons-bottom" role="img" aria-label="Small line-art icons of a chart, coin stacks and a calculator"></div>

  <p class="author"><span class="author-first">Tomas</span> <span class="author-last">Brennick</span></p>
</main>
</body>
</html>
```